QVB Commercial Roof Restoration LLC needs billboard and banner designs

Need billboard ad design for small commercial roof restoration company. Looking for a billboard design that can be used on digital and hard print billboards. Also need banner design for 4' x 8' job site banners that will go by roadside to draw potential customers to our brand. Our vision for bill board would show an attractive women in business dress, clearly in a building having to use an (red) umbrella (inside building) due to leaking roof. Caption "WE CAN HELP" www.QVBCOMMERCIALROOF.example
For banner design we would use some before/after roof photos (attached, blend/overlay at an angle) in background with "Another Quality Commercial Roof Restoration By:" "QVB Commercial Roof LLC" "Is your commercial roof leaking? Call 555.314.0827 for help".
All final designs should communicate commercial roof restoration only.
Target Market(s)
Commercial building owner/managers
Industry/Entity Type
Roofing
Requirements
Must have
- Just added a Jpeg file of a logo of the company that we buy our products from. This logo & "Certified Premier Installers" needs to be added to the project. It only needs to have a small footprint on the ad. Contact me if you have questions. Thank you.
Nice to have
- Billboard design; our name, website, relay our message with image. As described above in project description
Banner; Our name, phone number and bold written message

```html
<!DOCTYPE html>
<html lang="en">
<head>
<meta charset="utf-8">
<title>QVB Commercial Roof Restoration – Billboard</title>
<link rel="stylesheet" href="https://fonts.googleapis.com/css2?family=Open+Sans:wght@600;700;800&display=swap">
<style>
  :root {
    --page: #ffffff;
    --brand-red: #c4281c;
    --brand-blue: #0d4ea6;
    --ink-grey: #414141;
    --white: #ffffff;
    --roof-light: #f3f3f2;
    --roof-mid: #e4e3e1;
    --sky-top: #6f7884;
    --sky-low: #c9ced6;
    --roof-white: #eef1f4;
  }
  html, body {
    margin: 0;
    width: 1200px;
    height: 1200px;
    overflow: hidden;
    background: var(--page);
  }
  .billboard {
    position: absolute;
    left: 50px;
    top: 326px;
    width: 1100px;
    height: 548px;
    filter: drop-shadow(0 4px 10px rgba(0,0,0,0.25));
  }
  .billboard text {
    font-family: "Open Sans", Arial, sans-serif;
  }
  .brand-name { fill: var(--brand-blue); font-weight: 800; font-size: 30px; }
  .headline-red { fill: var(--brand-red); font-weight: 700; }
  .headline-blue { fill: var(--brand-blue); font-weight: 700; }
  .callout { fill: var(--white); font-weight: 700; }
  .web-address { fill: var(--ink-grey); font-weight: 700; }
</style>
</head>
<body>
<svg class="billboard" viewBox="0 0 1535 765" xmlns="http://www.w3.org/2000/svg">
  <defs>
    <linearGradient id="roofBackdrop" x1="0" y1="0" x2="1" y2="1">
      <stop offset="0" stop-color="var(--roof-mid)"/>
      <stop offset="0.5" stop-color="var(--roof-light)"/>
      <stop offset="1" stop-color="var(--roof-mid)"/>
    </linearGradient>
    <linearGradient id="finishedRoof" x1="0" y1="0" x2="0" y2="1">
      <stop offset="0" stop-color="var(--sky-top)"/>
      <stop offset="0.34" stop-color="var(--sky-low)"/>
      <stop offset="0.37" stop-color="#3a3d40"/>
      <stop offset="0.39" stop-color="var(--roof-white)"/>
      <stop offset="1" stop-color="#dfe4ea"/>
    </linearGradient>
    <clipPath id="panelClip"><rect width="1535" height="765"/></clipPath>
  </defs>

  <g clip-path="url(#panelClip)">
    <rect class="backdrop-photo" width="1535" height="765" fill="url(#roofBackdrop)"
          role="img" aria-label="Faded photo of a weathered corrugated metal commercial roof"/>

    <rect class="callout-band" x="0" y="530" width="1010" height="125" fill="var(--brand-blue)"/>

    <ellipse class="arc-blue" cx="1453" cy="382" rx="528" ry="466" fill="var(--brand-blue)"/>
    <ellipse class="arc-red" cx="1453" cy="382" rx="503" ry="462" fill="var(--brand-red)"/>
    <ellipse class="arc-gap" cx="1453" cy="382" rx="483" ry="463" fill="var(--white)"/>
    <ellipse class="result-photo" cx="1453" cy="382" rx="470" ry="469" fill="url(#finishedRoof)"
             role="img" aria-label="Photo of a restored white-coated metal roof under a cloudy sky with power lines"/>
  </g>

  <g class="brand-mark">
    <rect x="62" y="48" width="26" height="26" fill="var(--brand-red)"/>
    <text class="brand-name" x="100" y="72">QVB</text>
    <text class="brand-name" x="62" y="128" textLength="255" lengthAdjust="spacingAndGlyphs">COMMERCIAL</text>
    <text class="brand-name" x="62" y="166" textLength="255" lengthAdjust="spacingAndGlyphs">ROOF RESTORATION</text>
  </g>

  <g class="headline">
    <text class="headline-red" x="57" y="295" font-size="108" textLength="797" lengthAdjust="spacingAndGlyphs">COMMERCIAL</text>
    <text class="headline-blue" x="57" y="375" font-size="77" textLength="800" lengthAdjust="spacingAndGlyphs">ROOF RESTORATION</text>
    <text class="headline-red" x="55" y="500" font-size="160" textLength="796" lengthAdjust="spacingAndGlyphs">COMPANY</text>
  </g>

  <text class="callout" x="60" y="635" font-size="124" textLength="772" lengthAdjust="spacingAndGlyphs">WE CAN HELP</text>

  <text class="web-address" x="58" y="740" font-size="62" textLength="905" lengthAdjust="spacingAndGlyphs">www.QVBCOMMERCIALROOF.example</text>
</svg>
</body>
</html>
```